Brochure Design Project-Vornet

We are looking to design a bi-fold piece use for marketing to decision makers in the banking industry. I will have text shortly, but I'm trying to find a range for the design work. Our currently website is www.vornet-example.com, we are working on an updated site now.
TEXT:
Vornet + Associates PC provides tailored and focused service in a variety of practice areas, but maintains a strong concentration on a variety of real estate matters and representation. We strive to provide exceptional service to the real estate industry as well as to individual clients everyday.
TEXTLigris + Associates PC is a dynamic boutique law firm, concentrating on real estate matters and representation in the Commonwealth of Massachusetts and State of Conneticut. We take particular pride in our attention and obsession to detail and client service. The firm’s culture and organization is based on a team oriented approach, by which attorneys, support staff and paralegals work as a team to accomplish our top priority: outstanding client support and service.
The firm focuses on the representation of buyers, sellers, developers and lenders dealing with and working on residential real estate matters. All closings, purchases and refinance transactions are always conducted by Massachusetts Attorneys and attention to detail is our utmost priority. It is this obsessive attention to details and service that leads to long term client relationships. Our clients range from developers of Condominium projects in the Greater Boston area to first time homebuyer’s purchasing their first Condominium. Regardless of the scope of representation or the magnitude of the transaction, our staff and attorney’s work with our clients to assist them throughout the transaction and ensure a smooth closing.
Our Lender clients find that an attorney is always available to discuss their individual needs and our commitment to implementing and using the finest and most sophisticated technology allows us to interact with lenders, borrowers and clients in a fast and effective way. We appreciate that lender–borrower relationships are important not only for customer satisfaction but for business growth. We know that our service is a reflection of the lender and we constantly strive to exceed the expectations of all parties.
Vornet + Associates PC is an authorized issuing agent of title insurance for Harrowgate Deed Assurance of Ohio and Brinsley Title Insurance Company and Title Meridor Group. We maintain strong and committed relationships with underwriting counsel and work with the title insurers to prevent problems and establish creative solutions for our clients in this rapid paced real estate marketplace.
- Outstanding Service
- Data Security
- Data Redundancy and Safeguards
- Priority underwriting
- Cyber-theft Insurance Coverage
- High limit E&O coverage
Reason: I'm extending the timeline because of my delay in getting draft text. I have also increased the budget. Please let me know if I am close to a budget number that would appeal to you.
Reason: Due to travel, I will need to extend the final deadline by 2 days.
Target Market(s)
Chief Legal Officers, Banking Industry
Industry/Entity Type
Real Estate
Look and feel
Each slider illustrates characteristics of the customer's brand and the style your logo design should communicate.

```html
<!DOCTYPE html>
<html lang="en">
<head>
<meta charset="utf-8">
<title>Vornet + Associates PC — Bi-fold Brochure Spread</title>
<link rel="stylesheet" href="https://fonts.googleapis.com/css2?family=Arimo:wght@400;700&display=swap">
<style>
  :root {
    --backdrop: #e9e7e2;
    --paper: #f7f7f5;
    --ink: #3f4240;
    --green: #8db567;
    --green-deep: #7aa553;
    --green-box: rgba(135, 178, 98, 0.92);
    --tag-grey: #dcdfd9;
    --band-grey: #e1e4de;
    --photo-warm: #c2511c;
    --photo-dark: #3a1a0c;
    --photo-house: #7f9c6a;
    --photo-sky: #9cc2e0;
  }
  * { box-sizing: border-box; margin: 0; padding: 0; }
  html, body {
    width: 1200px; height: 573px; overflow: hidden;
    background: var(--backdrop);
    font-family: "Arimo", Arial, sans-serif;
    color: var(--ink);
  }
  .spread {
    position: absolute; left: 100px; top: 36px;
    width: 1000px; height: 500px;
    display: flex;
    box-shadow: 0 6px 22px rgba(0,0,0,0.18);
  }
  .page {
    position: relative; width: 500px; height: 500px;
    background: var(--paper); overflow: hidden;
  }
  .page--left { border-right: 1px solid #d6d8d3; }
  .page__footer-band {
    position: absolute; left: 0; right: 0; bottom: 0; height: 14px;
    background: var(--green);
  }
  .intro {
    font-size: 11.5px; line-height: 1.5; text-align: justify;
  }
  .page--left .content { padding: 30px 30px 0; }
  .intro--highlight {
    background: var(--band-grey);
    border-left: 6px solid var(--green);
    padding: 8px 10px;
    margin-bottom: 10px;
  }
  .intro + .intro { margin-bottom: 10px; }
  .intro__photo {
    float: left; width: 140px; height: 82px;
    margin: 4px 12px 4px 0;
    background: linear-gradient(180deg, var(--photo-sky) 0%, var(--photo-sky) 30%, #b0694a 45%, var(--photo-house) 80%, #5d7d45 100%);
  }
  .page--right .hero-photo {
    position: absolute; left: 0; top: 0; width: 500px; height: 150px;
    background: radial-gradient(ellipse at 35% 55%, var(--photo-warm) 0%, #8a2f10 55%, var(--photo-dark) 100%);
  }
  .lender-box {
    position: absolute; left: 36px; right: 20px; top: 122px;
    background: var(--green-box);
    color: #ffffff;
    padding: 12px 14px;
    font-size: 11px; line-height: 1.5; text-align: justify;
  }
  .lender-box p + p { margin-top: 9px; }
  .features {
    position: absolute; left: 40px; right: 24px; top: 366px;
    display: flex; justify-content: space-between;
    list-style: none;
  }
  .features__column { display: flex; flex-direction: column; gap: 7px; }
  .features__column--right { margin-top: -16px; align-items: flex-end; }
  .feature-tag {
    display: inline-block;
    background: var(--tag-grey);
    border-left: 5px solid var(--green-deep);
    padding: 3px 12px 3px 8px;
    font-size: 12px; color: #2f3230;
    white-space: nowrap;
  }
  .features__column--left .feature-tag:nth-child(1) { margin-left: 14px; }
  .features__column--left .feature-tag:nth-child(2) { margin-left: 34px; }
</style>
</head>
<body>
  <main class="spread">
    <section class="page page--left">
      <div class="content">
        <p class="intro intro--highlight">Vornet + Associates PC provides tailored and focused service in a variety of practice areas, but maintains a strong concentration on a variety of real estate matters and representation. We strive to provide exceptional service to the real estate industry as well as to individual clients everyday.</p>
        <p class="intro">Vornet + Associates PC is a dynamic boutique law firm, concentrating on real estate matters and representation in the Commonwealth of Massachusetts and State of Connecticut. We take particular pride in our attention and obsession to detail and client service. The firm’s culture and organization is based on a team oriented approach, by which attorneys, support staff and paralegals work as a team to accomplish our top priority: outstanding client support and service.</p>
        <div class="intro__photo" role="img" aria-label="Photo of a row of brick townhouses behind a white fence"></div>
        <p class="intro">The firm focuses on the representation of buyers, sellers, developers and lenders dealing with and working on residential real estate matters. All closings, purchases and refinance transactions are always conducted by Massachusetts Attorneys and attention to detail is our utmost priority. It is this obsessive attention to details and service that leads to long term client relationships. Our clients range from developers of Condominium projects in the Greater Boston area to first time homebuyer’s purchasing their first Condominium. Regardless of the scope of representation or the magnitude of the transaction, our staff and attorney’s work with our clients to assist them throughout the transaction and ensure a smooth closing.</p>
      </div>
      <div class="page__footer-band"></div>
    </section>

    <section class="page page--right">
      <div class="hero-photo" role="img" aria-label="Photo of a judge's gavel on a warm orange background"></div>
      <div class="lender-box">
        <p>Our Lender clients find that an attorney is always available to discuss their individual needs and our commitment to implementing and using the finest and most sophisticated technology allows us to interact with lenders, borrowers and clients in a fast and effective way. We appreciate that lender–borrower relationships are important not only for customer satisfaction but for business growth. We know that our service is a reflection of the lender and we constantly strive to exceed the expectations of all parties.</p>
        <p>Vornet + Associates PC is an authorized issuing agent of title insurance for Harrowgate Deed Assurance of Ohio and Brinsley Title Insurance Company and Title Meridor Group. We maintain strong and committed relationships with underwriting counsel and work with the title insurers to prevent problems and establish creative solutions for our clients in this rapid paced real estate marketplace.</p>
      </div>
      <div class="features">
        <div class="features__column features__column--left">
          <span class="feature-tag">Outstanding Service</span>
          <span class="feature-tag">Data Security</span>
          <span class="feature-tag">Data Redundancy and Safeguards</span>
        </div>
        <div class="features__column features__column--right">
          <span class="feature-tag">Priority underwriting</span>
          <span class="feature-tag">Cyber-theft Insurance Coverage</span>
          <span class="feature-tag">High limit E&amp;O coverage</span>
        </div>
      </div>
      <div class="page__footer-band"></div>
    </section>
  </main>
</body>
</html>
```